Business Cards and Stationary for Harbor Chapel
Harbor Chapel
Business Cards and Stationary for Harbor Chapel - Religion and Spirituality
Creative Brief
Professional
Marvela Quinby
Pastor
P O Box 517 Ellenwood, Georgia 30417
1harborchapel@examplemail.com
Please note: phone number ar dummy numbers should have correct number before project ends
MarvelaK MarvelaK
PixelQuarry.com, Thanks for your platform that assist ALL of us in getting it done. MarvelaK
Only 2 Hours to go and this project will close. Please let me take this time to say Thanks to each of the designers who uploaded drafts and revisions. There were many designs for me to chooses from. To those who really were patient with me and allowed me to assist you through private messages in order to get the designs where I wanted them, THANKS! This was my 2nd project and I must say that you designers really made it easy for me. Although I can only select one Winner, each of your designs were awesome. Thanks for such a great experience. MarkCraftPeak You guys Rock! Thanks for being here for the REGULAR FOLK. This web site and the Designers are really a God Given Gift to the word. THANKS! MarvelaK
Designers thanks so much for your uploads drafts so far. I'm being presented with a lot of creativity and options. For those who recently upload drafts, I will be reviewing those today and providing feedback private where when necessary. I will also eliminate theses drafts there are heading in the wrong direction for this project. Please continue to upload drafts and again Thanks! MarvelaK
velkordraws velkordraws
Changes noted Thanks
Designers, Thanks so much for each of you who have uploaded drafts so far. I would like you to add the following to your drafts. Front - Web Address use www. 1harborchapel.com for drafts Back - Facebook - Twitter - YouTube Can I also see what an email signature might look like. thanks in advance for the modifications. MarvelaK

```html
<!DOCTYPE html>
<html lang="en">
<head>
<meta charset="utf-8">
<title>Harbor Chapel Stationery Concepts</title>
<link rel="stylesheet" href="https://fonts.googleapis.com/css2?family=Libre+Baskerville:wght@400;700&family=Open+Sans:wght@400;600&display=swap">
<style>
:root{
  --maroon:#6c1515;
  --slate:#4b4b4d;
  --paper:#ffffff;
  --paper-soft:#f1f1f1;
  --ink:#555;
  --ground:#c9a97f;
  --label:#2d2116;
}
*{margin:0;padding:0;box-sizing:border-box}
html,body{width:1200px;height:274px;overflow:hidden;background:var(--ground)}
.canvas{position:relative;width:1200px;height:274px;font-family:"Open Sans",sans-serif;color:var(--ink)}
.piece{position:absolute;background:var(--paper);overflow:hidden;box-shadow:0 1px 3px rgba(0,0,0,.35)}
.label{position:absolute;font-family:"Libre Baskerville",serif;font-size:4.4px;color:var(--label);text-align:center;white-space:nowrap}
.wave{position:absolute;left:0;bottom:0;width:100%}
.brand{position:absolute;display:flex;align-items:center;gap:2px;font-family:"Libre Baskerville",serif;color:var(--maroon)}
.brand .dot{border-radius:50%;background:var(--maroon);flex:none}
.brand .name{font-weight:700;line-height:1;letter-spacing:.04em;text-transform:uppercase;white-space:nowrap}
.brand.light{color:var(--paper)}
.brand.light .dot{background:var(--paper)}
.tiny{position:absolute;font-size:2.4px;line-height:1.45;color:var(--ink);white-space:nowrap}
.tiny.white{color:#fff}
.faint-disc{position:absolute;border-radius:50%;background:rgba(0,0,0,.06)}
.faint-disc.on-dark{background:rgba(255,255,255,.07)}
.person{position:absolute;font-family:"Libre Baskerville",serif;color:var(--maroon);text-align:center;line-height:1.2;white-space:nowrap}
.person small{display:block;font-family:"Open Sans",sans-serif;color:#777}
.social{position:absolute;font-size:2.5px;line-height:2.3;color:#fff;font-weight:600}
.social span{display:flex;align-items:center;gap:2px}
.social i{width:3px;height:3px;background:#eee;display:inline-block}
.fax-table{position:absolute;left:10px;width:158px;display:grid;grid-template-columns:21px 56px 23px 56px;gap:2px 1px;font-size:2.6px}
.fax-table div{background:#ececec;height:6.5px;line-height:6.5px;padding-left:2px}
.checks{position:absolute;left:10px;display:flex;gap:9px;font-size:2.2px}
.checks span::before{content:"";display:inline-block;width:3px;height:3px;border:.3px solid #777;margin-right:1px;vertical-align:-.6px}
.body-text{position:absolute;font-size:2.5px;line-height:1.5;color:#666}
.body-text p{margin-bottom:3px}
.envelope{position:absolute;background:var(--paper);box-shadow:0 1px 3px rgba(0,0,0,.35)}
.flap{position:absolute;left:0;top:0;width:100%}
.seal{position:absolute;width:10px;height:10px;border-radius:50%;background:#fff}
.seal.dark{background:var(--maroon)}
.vert{position:absolute;font-size:2.4px;color:#ddd;writing-mode:vertical-rl;transform:rotate(180deg);letter-spacing:.05em;white-space:nowrap}
</style>
</head>
<body>
<main class="canvas">

  <!-- Business card front -->
  <section class="piece" style="left:10px;top:58px;width:105px;height:58px;border-radius:2px">
    <div class="brand" style="left:6px;top:6px">
      <div class="dot" style="width:7px;height:7px"></div>
      <div class="name" style="font-size:5.2px">Harbor<br>Chapel</div>
    </div>
    <svg class="wave" viewBox="0 0 100 40" preserveAspectRatio="none" style="height:36px">
      <path d="M0 19 C30 32 62 4 100 2 L100 40 L0 40Z" fill="var(--maroon)"/>
      <path d="M0 17 C30 30 62 2 100 0" fill="none" stroke="#999" stroke-width="1"/>
    </svg>
    <div class="tiny white" style="left:5px;top:31px;font-size:2.2px">P O Box 517<br>Larkmoor, Westhaven 30417<br>555.014.4445<br>555.014.4444<br>1harborchapel@examplemail.com<br>www.1harborchapel.com</div>
    <div class="person" style="right:6px;top:41px;font-size:4px;color:#fff">Marvela Quinby<small style="font-size:2.8px;color:#eee">Pastor</small></div>
  </section>
  <div class="label" style="left:10px;top:120px;width:105px">Front card Option_01</div>

  <!-- Business card backs -->
  <section class="piece" style="left:10px;top:133px;width:105px;height:58px;background:var(--maroon);border-radius:2px">
    <div class="faint-disc on-dark" style="left:55px;top:8px;width:52px;height:52px"></div>
    <div class="brand light" style="left:7px;top:6px">
      <div class="dot" style="width:6px;height:6px"></div>
      <div class="name" style="font-size:5.6px">Harbor<br>Chapel</div>
    </div>
    <div class="social" style="left:8px;top:33px"><span><i></i>pageshare.example</span><span><i></i>chirpline.example</span><span><i></i>clipstream.example</span></div>
  </section>
  <div class="label" style="left:10px;top:194px;width:105px">Back Card Option_01</div>

  <section class="piece" style="left:10px;top:201px;width:105px;height:58px;background:var(--maroon);border-radius:2px">
    <div class="faint-disc on-dark" style="left:52px;top:2px;width:56px;height:56px"></div>
    <div class="brand light" style="left:7px;top:6px">
      <div class="dot" style="width:6px;height:6px"></div>
      <div class="name" style="font-size:5.6px">Harbor<br>Chapel</div>
    </div>
    <div class="social" style="left:8px;top:33px"><span><i></i>pageshare.example</span><span><i></i>chirpline.example</span><span><i></i>clipstream.example</span></div>
  </section>
  <div class="label" style="left:10px;top:263px;width:105px">Back Card Option_02</div>

  <!-- Letterhead -->
  <section class="piece" style="left:122px;top:34px;width:175px;height:226px">
    <div class="faint-disc" style="left:50px;top:55px;width:88px;height:88px"></div>
    <div class="brand" style="left:12px;top:14px">
      <div class="dot" style="width:6px;height:6px"></div>
      <div class="name" style="font-size:4.2px">Harbor<br>Chapel</div>
    </div>
    <div class="tiny" style="left:128px;top:11px;font-size:2.2px">P O Box 517<br>Larkmoor, Westhaven 30417<br>555.014.4445<br>555.014.4444<br>1harborchapel@examplemail.com</div>
    <div class="tiny" style="left:12px;top:49px;font-size:3px;line-height:1.6">Date<br><br><b style="color:#333">Recipient Name</b><br><br>Company Name<br>Street Address<br>City, State, Zip</div>
    <div class="body-text" style="left:12px;top:92px;width:150px">
      <p>Thank you for joining our fellowship this season. We are grateful for your support and prayers as our church family grows in faith and service to the community.</p>
      <p>Our weekly gatherings continue each Sunday morning, with study groups meeting on Wednesday evenings at the chapel hall.</p>
      <p>Please let us know if you would like to volunteer for the upcoming outreach program.</p>
      <p>With gratitude and warm regards.</p>
    </div>
    <div class="tiny" style="left:12px;top:170px;font-size:2.6px">Sincerely,</div>
    <div role="img" aria-label="Handwritten signature" style="position:absolute;left:13px;top:176px;width:38px;height:9px;background:linear-gradient(90deg,#e8e8e8,#f6f6f6)"></div>
    <div class="person" style="left:24px;top:186px;font-size:3px;text-align:left">Marvela Quinby<small style="font-size:2.2px">Pastor</small></div>
    <svg class="wave" viewBox="0 0 100 40" preserveAspectRatio="none" style="height:22px">
      <path d="M0 30 C30 40 60 14 100 6 L100 40 L0 40Z" fill="var(--maroon)"/>
      <path d="M0 28 C30 38 60 12 100 4" fill="none" stroke="#888" stroke-width="1"/>
    </svg>
    <div class="tiny white" style="right:8px;bottom:4px;letter-spacing:.1em">www.1harborchapel.com</div>
  </section>
  <div class="label" style="left:122px;top:263px;width:175px">Letterhead option_01</div>

  <!-- Fax sheet -->
  <section class="piece" style="left:307px;top:34px;width:175px;height:226px">
    <div class="faint-disc" style="left:38px;top:110px;width:100px;height:100px"></div>
    <div class="brand" style="left:15px;top:14px">
      <div class="dot" style="width:6px;height:6px"></div>
      <div class="name" style="font-size:4.2px">Harbor<br>Chapel</div>
    </div>
    <div class="tiny" style="left:130px;top:11px;font-size:2.2px">P O Box 517<br>Larkmoor, Westhaven 30417<br>555.014.4445<br>555.014.4444<br>1harborchapel@examplemail.com</div>
    <div class="fax-table" style="top:43px">
      <div>To</div><div></div><div>From</div><div></div>
      <div>Fax</div><div></div><div>Pages</div><div></div>
      <div>Phone</div><div></div><div>Date</div><div></div>
      <div>Re</div><div></div><div>CC</div><div></div>
    </div>
    <div class="checks" style="top:80px"><span>Urgent</span><span>For Review</span><span>Please comment</span><span>Please reply</span><span>Please recycle</span></div>
    <div class="tiny" style="left:11px;top:88px;font-size:3px">Comments :</div>
    <svg class="wave" viewBox="0 0 100 40" preserveAspectRatio="none" style="height:22px">
      <path d="M0 30 C30 40 60 14 100 6 L100 40 L0 40Z" fill="#111"/>
      <path d="M0 28 C30 38 60 12 100 4" fill="none" stroke="#888" stroke-width="1"/>
    </svg>
    <div class="tiny white" style="right:8px;bottom:4px;letter-spacing:.1em">www.1harborchapel.com</div>
  </section>

  <!-- Title -->
  <div class="brand" style="left:503px;top:56px">
    <div class="dot" style="width:13px;height:13px"></div>
    <div class="name" style="font-size:9.5px">Harbor<br>Chapel</div>
  </div>
  <div class="label" style="left:500px;top:87px;width:102px;font-size:7.6px;color:#1c140c">Stationary Concepts</div>

  <!-- Email signature 01 -->
  <section class="piece" style="left:490px;top:109px;width:116px;height:56px">
    <div class="brand" style="left:17px;top:17px">
      <div class="dot" style="width:6px;height:6px"></div>
      <div class="name" style="font-size:4.4px">Harbor<br>Chapel</div>
    </div>
    <div class="person" style="left:70px;top:6px;font-size:3.2px;text-align:left">Marvela Quinby<small style="font-size:2.2px">Pastor</small></div>
    <div class="tiny" style="left:70px;top:17px;font-size:2.2px">P O Box 517<br>Larkmoor, Westhaven 30417<br>555.014.4445<br>555.014.4444<br>1harborchapel@examplemail.com</div>
    <svg class="wave" viewBox="0 0 100 40" preserveAspectRatio="none" style="height:14px">
      <path d="M0 8 C30 40 60 22 100 6 L100 40 L0 40Z" fill="var(--maroon)"/>
      <path d="M0 6 C30 38 60 20 100 4" fill="none" stroke="#888" stroke-width="1.4"/>
    </svg>
    <div class="tiny white" style="right:4px;bottom:2px;letter-spacing:.08em">www.1harborchapel.com</div>
  </section>
  <div class="label" style="left:490px;top:169px;width:116px">Email Signature_01</div>

  <!-- Email signature 02 -->
  <section class="piece" style="left:616px;top:86px;width:62px;height:78px">
    <div class="brand" style="left:9px;top:10px">
      <div class="dot" style="width:5px;height:5px"></div>
      <div class="name" style="font-size:4px">Harbor<br>Chapel</div>
    </div>
    <div class="person" style="left:0;width:62px;top:30px;font-size:3px">Marvela Quinby<small style="font-size:2.2px">Pastor</small></div>
    <div class="tiny" style="left:0;width:62px;top:42px;font-size:2px;text-align:center">P O Box 517<br>Larkmoor, Westhaven 30417<br>P: 555.014.4445 C: 555.014.4444<br>E: 1harborchapel@examplemail.com</div>
    <svg class="wave" viewBox="0 0 100 40" preserveAspectRatio="none" style="height:13px">
      <path d="M0 22 C30 40 60 10 100 4 L100 40 L0 40Z" fill="var(--maroon)"/>
      <path d="M0 20 C30 38 60 8 100 2" fill="none" stroke="#888" stroke-width="1.4"/>
    </svg>
    <div class="tiny white" style="right:4px;bottom:1px">www.1harborchapel.com</div>
  </section>
  <div class="label" style="left:616px;top:169px;width:62px">Email Signature_02</div>

  <!-- Envelope front -->
  <section class="piece" style="left:490px;top:178px;width:189px;height:82px">
    <div class="brand" style="left:9px;top:8px">
      <div class="dot" style="width:6px;height:6px"></div>
      <div class="name" style="font-size:4.4px">Harbor<br>Chapel</div>
    </div>
    <div class="tiny" style="left:23px;top:21px;font-size:2.3px">P O Box 517, Larkmoor<br>Westhaven 30417</div>
  </section>
  <div class="label" style="left:490px;top:263px;width:189px">Envelope  Front</div>

  <!-- Envelope backs -->
  <section class="envelope" style="left:714px;top:89px;width:187px;height:82px">
    <svg class="flap" viewBox="0 0 187 30" preserveAspectRatio="none" style="height:28px">
      <path d="M0 0 H187 L185 24 Q184 28 180 28 H7 Q3 28 2 24Z" fill="var(--maroon)"/>
    </svg>
    <div class="seal" style="left:88px;top:8px"></div>
  </section>
  <section class="envelope" style="left:702px;top:133px;width:187px;height:82px">
    <svg class="flap" viewBox="0 0 187 30" preserveAspectRatio="none" style="height:28px">
      <path d="M0 0 H187 L185 24 Q184 28 180 28 H7 Q3 28 2 24Z" fill="var(--slate)"/>
    </svg>
    <div class="seal" style="left:88px;top:8px"></div>
  </section>
  <section class="envelope" style="left:689px;top:178px;width:189px;height:82px">
    <svg class="flap" viewBox="0 0 189 82" preserveAspectRatio="none" style="height:82px">
      <path d="M0 82 L80 44 M189 82 L109 44" stroke="#ddd" stroke-width=".6" fill="none"/>
      <path d="M1 0 H188 L187 22 Q186 27 181 27 H8 Q3 27 2 22Z" fill="var(--paper-soft)" stroke="#ccc" stroke-width=".5"/>
    </svg>
    <div class="seal dark" style="left:89px;top:9px"></div>
  </section>
  <div class="label" style="left:689px;top:263px;width:212px">Envelope  Back</div>

  <!-- Folder -->
  <section class="piece" style="left:912px;top:39px;width:278px;height:222px;background:transparent;box-shadow:none;overflow:visible">
    <div style="position:absolute;left:0;top:0;width:20px;height:160px;background:var(--slate)"></div>
    <div style="position:absolute;left:20px;top:0;width:119px;height:222px;background:var(--maroon);box-shadow:0 1px 3px rgba(0,0,0,.35)">
      <div class="faint-disc on-dark" style="left:30px;top:35px;width:75px;height:75px"></div>
      <div class="tiny white" style="left:0;top:135px;font-size:2.3px">P O Box 517<br>Larkmoor, Westhaven 30417<br>555.014.4445<br>555.014.4444<br>1harborchapel@examplemail.com</div>
    </div>
    <div class="vert" style="left:6px;top:25px">www.1harborchapel.com</div>
    <div style="position:absolute;left:139px;top:0;width:128px;height:222px;background:var(--paper);box-shadow:0 1px 3px rgba(0,0,0,.35)">
      <div class="brand" style="left:22px;top:74px">
        <div class="dot" style="width:12px;height:12px"></div>
        <div class="name" style="font-size:9px">Harbor<br>Chapel</div>
      </div>
      <svg viewBox="0 0 128 90" preserveAspectRatio="none" style="position:absolute;left:0;bottom:0;width:128px;height:90px">
        <path d="M0 10 C40 -2 80 22 128 16 L128 90 L0 90Z" fill="var(--maroon)"/>
        <path d="M0 8 C40 -4 80 20 128 14" fill="none" stroke="#888" stroke-width="1"/>
      </svg>
      <div style="position:absolute;left:44px;top:197px;width:50px;height:24px;background:#fff;transform:rotate(-12deg);box-shadow:0 1px 2px rgba(0,0,0,.4)">
        <div class="brand" style="left:3px;top:9px"><div class="dot" style="width:3px;height:3px"></div><div class="name" style="font-size:2.6px">Harbor Chapel</div></div>
        <div class="person" style="left:30px;top:3px;font-size:1.8px">Marvela Quinby</div>
      </div>
    </div>
    <div style="position:absolute;left:267px;top:0;width:11px;height:160px;background:var(--slate)"></div>
    <div class="vert" style="left:270px;top:25px">www.1harborchapel.com</div>
  </section>
  <div class="label" style="left:1000px;top:263px;width:100px">Folder</div>

</main>
</body>
</html>
```